VARDO Web

To design a look and feel for a website. The company offers technical services to governemtns and public bodies. It does NOT market to the public.

The core business is GIS (Geographic Information Systems)

The site needs to be clean and simple, The current version is available here: www.varduna.ie

Target Market(s)

Goverment agencies and public bodies in the EU, buying through the public procurerment process

Requirements
Should not have
• corny graphics of hands holding globes or sateliites please.

```html
<!DOCTYPE html>
<html lang="en">
<head>
<meta charset="utf-8">
<title>VARDO Web</title>
<link href="https://fonts.googleapis.com/css2?family=Roboto:wght@300;400;500&display=swap" rel="stylesheet">
<style>
:root{
  --accent:#8b87c0;
  --navy:#233f7e;
  --text:#555;
  --muted:#777;
  --footer:#aeb0d4;
  --line:#e4e4e4;
}
*{margin:0;padding:0;box-sizing:border-box}
html,body{width:1159px;height:1200px;overflow:hidden}
body{position:relative;background:#fff;font-family:'Roboto',sans-serif;color:var(--text)}
.topbar{position:absolute;left:0;top:0;width:1159px;height:5px;background:var(--accent)}
.header{position:absolute;left:0;top:5px;width:1159px;height:117px;background:#fff;box-shadow:0 2px 6px rgba(0,0,0,.06);z-index:2}
.brand{position:absolute;left:126px;top:32px;display:flex;align-items:center;gap:8px}
.brand-dot{width:12px;height:12px;border-radius:50%;background:var(--accent)}
.brand-name{font-size:26px;font-weight:500;color:var(--navy);letter-spacing:1px}
.brand-sub{position:absolute;left:126px;top:92px;font-size:12px;font-weight:300;color:var(--accent)}
.nav{position:absolute;right:125px;top:52px;display:flex;list-style:none}
.nav li{font-size:14px;color:var(--text);padding:0 19px;height:36px;line-height:36px;position:relative}
.nav li:last-child{padding-right:0}
.nav li.active{background:var(--navy);color:#fff;border-radius:2px;padding:0 16px;margin-right:3px}
.nav li.active::after{content:"";position:absolute;left:50%;bottom:-6px;margin-left:-6px;border:6px solid transparent;border-bottom:0;border-top-color:var(--navy)}
.hero{position:absolute;left:0;top:122px;width:1159px;height:424px;background:linear-gradient(#fff,#e5e5e5)}
.hero-title{position:absolute;left:126px;top:90px;font-size:35px;font-weight:500;color:var(--navy);letter-spacing:.5px}
.hero-sub{position:absolute;left:126px;top:138px;font-size:24px;font-weight:400;color:#555;line-height:34px;letter-spacing:.5px}
.hero-btn{position:absolute;left:127px;top:213px;width:135px;height:40px;background:#9c98cc;border:1px solid #8b87c0;color:#fff;font-size:16px;line-height:38px;text-align:center;letter-spacing:.5px}
.dots{position:absolute;left:125px;top:281px;display:flex;gap:6px}
.dots span{width:15px;height:15px;border-radius:50%;background:#999}
.dots span:first-child{background:#666}
.hero-frame{position:absolute;left:536px;top:68px;width:498px;height:307px;background:#fff;border:1px solid #ddd;padding:5px;box-shadow:0 1px 3px rgba(0,0,0,.1)}
.hero-photo{width:100%;height:100%;background:linear-gradient(100deg,#c9a876 0%,#d9c79a 30%,#cfd394 55%,#b7a27a 80%,#3b3a44 100%)}
.news{position:absolute;left:126px;top:565px;width:908px;height:70px;border:1px solid var(--line);background:#fcfcfc;display:flex;align-items:center}
.news-label{margin-left:26px;font-size:18px;color:var(--accent);width:141px}
.news-item{font-size:12.5px;color:#555}
.news-date{color:var(--navy)}
.news-more{font-style:italic;color:var(--navy);font-size:11px;font-weight:500}
.news-arrows{position:absolute;right:20px;top:25px;display:flex;gap:16px}
.welcome{position:absolute;left:126px;top:662px;width:590px}
.welcome h2,.services h2{font-size:23px;font-weight:400;color:var(--accent);letter-spacing:.3px}
.welcome p{font-size:13px;line-height:22.3px;color:#555;margin-top:10px}
.welcome h2+p{margin-top:14px}
.btn{display:inline-block;background:var(--navy);color:#fff;font-size:12px;height:30px;line-height:30px;padding:0 13px;border-radius:2px}
.welcome .btn{margin-top:24px}
.services{position:absolute;left:744px;top:667px;width:290px;height:277px;border:1px solid var(--line);background:#fbfbfb;padding:14px 20px}
.services ul{list-style:none;margin-top:10px}
.services li{font-size:13px;color:#555;height:23.2px;display:flex;align-items:center;gap:13px}
.services .btn{margin-top:9px}
.partners{position:absolute;left:0;top:974px;width:1159px;height:103px;background:#fff;border-top:1px solid #eee;display:flex;align-items:center;justify-content:space-between;padding:0 125px 0 126px}
.partner{display:flex;align-items:center;gap:7px;font-size:16px;color:#666;line-height:18px}
.partner i{width:34px;height:34px;border-radius:50%;background:#888;flex:none}
.footer{position:absolute;left:0;top:1077px;width:1159px;height:123px;background:var(--footer)}
.footer-nav{position:absolute;left:126px;top:29px;display:flex;gap:35px;list-style:none;font-size:13px;color:#fff}
.copyright{position:absolute;left:126px;top:73px;font-size:12px;color:var(--navy);letter-spacing:.2px}
.copyright span{color:#fff}
.social{position:absolute;right:125px;top:33px;display:flex;gap:8px}
.social span{width:30px;height:30px;border-radius:3px;background:var(--navy);color:#fff;font-size:8px;display:flex;align-items:center;justify-content:center}
</style>
</head>
<body>
<div class="topbar"></div>
<header class="header">
  <div class="brand"><span class="brand-dot"></span><span class="brand-name">VARDO</span></div>
  <div class="brand-sub">Information Expertise</div>
  <ul class="nav">
    <li class="active">Home</li><li>About Us</li><li>Services</li><li>Clients</li><li>Inspire</li><li>Contact</li>
  </ul>
</header>

<section class="hero">
  <h1 class="hero-title">VARDO Service Include</h1>
  <p class="hero-sub">Spatial System Development<br>and maintenance..</p>
  <div class="hero-btn">READ MORE</div>
  <div class="dots"><span></span><span></span><span></span><span></span></div>
  <div class="hero-frame"><div class="hero-photo" role="img" aria-label="Presenter pointing at a projected GIS map to a seated audience"></div></div>
</section>

<div class="news">
  <div class="news-label">Latest News:</div>
  <div class="news-item"><span class="news-date">Dec 22, 2013----</span> The Lanark Heritage Board launches Landmark Viewer... <span class="news-more">Read More</span></div>
  <div class="news-arrows">
    <svg width="12" height="20" viewBox="0 0 12 20"><path d="M10 2 2 10l8 8" fill="none" stroke="#666" stroke-width="1.6"/></svg>
    <svg width="12" height="20" viewBox="0 0 12 20"><path d="M2 2l8 8-8 8" fill="none" stroke="#666" stroke-width="1.6"/></svg>
  </div>
</div>

<section class="welcome">
  <h2>Welcome to Our Company Website</h2>
  <p>The VARDO Group has been in business since 1994 and continues to develop and update its range of services. The company has a high level of expertise in handling data and information, and in building and re-engineering database systems. We have a particular expertise in working with Irish data sets and have a strong grounding in dealing with spatial data.</p>
  <p>We also have extensive experience in working in a Kestrel development environment, both Desktop and KSP.NET.We have worked on development of small scale systems using Kestrel products for over 12 years. We have assisted in the migration of systems from Kestrel Base to both Kestrel Data Server and Orvane databases. This has included re-writing code from KBA to either KB.Net or KScript.</p>
  <span class="btn">READ MORE</span>
</section>

<aside class="services">
  <h2>Our Services</h2>
  <ul>
    <li><svg width="13" height="11" viewBox="0 0 13 11"><path d="M1 6l4 4 7-9" fill="none" stroke="#233f7e" stroke-width="2.2"/></svg>GIS Data Capture &amp; Training</li>
    <li><svg width="13" height="11" viewBox="0 0 13 11"><path d="M1 6l4 4 7-9" fill="none" stroke="#233f7e" stroke-width="2.2"/></svg>Document Scanning</li>
    <li><svg width="13" height="11" viewBox="0 0 13 11"><path d="M1 6l4 4 7-9" fill="none" stroke="#233f7e" stroke-width="2.2"/></svg>Data Capture</li>
    <li><svg width="13" height="11" viewBox="0 0 13 11"><path d="M1 6l4 4 7-9" fill="none" stroke="#233f7e" stroke-width="2.2"/></svg>GIS Data Capture &amp; Training</li>
    <li><svg width="13" height="11" viewBox="0 0 13 11"><path d="M1 6l4 4 7-9" fill="none" stroke="#233f7e" stroke-width="2.2"/></svg>Document Scanning</li>
    <li><svg width="13" height="11" viewBox="0 0 13 11"><path d="M1 6l4 4 7-9" fill="none" stroke="#233f7e" stroke-width="2.2"/></svg>Data Capture</li>
    <li><svg width="13" height="11" viewBox="0 0 13 11"><path d="M1 6l4 4 7-9" fill="none" stroke="#233f7e" stroke-width="2.2"/></svg>GIS Data Capture &amp; Training</li>
  </ul>
  <span class="btn">READ MORE</span>
</aside>

<section class="partners">
  <div class="partner"><i></i>Terrane<br>Land Office</div>
  <div class="partner"><i></i>Ashmoor<br>County Council</div>
  <div class="partner"><i></i>Westfold<br>County Council</div>
  <div class="partner"><i></i>Riverlands<br>Agency</div>
  <div class="partner"><i></i>Meridian<br>Survey</div>
</section>

<footer class="footer">
  <ul class="footer-nav"><li>Home</li><li>About Us</li><li>Services</li><li>Clients</li><li>Inspire</li><li>Contact</li></ul>
  <div class="social"><span>Pinlo</span><span>Chirra</span><span>Linkra</span><span>Vidzo</span></div>
  <p class="copyright">Copyright © 2013. <span>The VARDO Group</span>. All Right Reserved</p>
</footer>
</body>
</html>
```